MCP phase 1 web design

Meridale Capital Partners Ltd (MCP) is a challenger business to the traditional leasing market. We look for solutions to complex problems involving the funding of capital equipment within an office environment and then build documentation around the solution. We recently created a brief for a logo and successfully completed that assignment. We now need to create our first web site which is simply intended to be informative. To help interested designers we have attached a detailed brief that is broken into three sections. The first explains how we see the site developing over time from something quite straightforward initially to a full transaction capability. Whoever wins this competition will be expected to work with us into the future to help develop the site. Section 2 gives you a view about our likes and dislikes by reviewing some existing sites. Section 3 gives you the structure and content of the site based upon our likes and dislikes. We are by no means committed to the structure and if you believe it can be presented in a better way then please use your design. The text is fixed as content. The images to appear can be anything from photographs to line drawings again entirely at the designers whim. Currently we have a home page plus 5 subsidiary pages. A few things to help you:
1. The logo is fixed and should be amongst the downloads.
2. The colours we have are corporate and should be used.
3. The typeface we use within the business is "Verdana"
Good luck.

```html
<!DOCTYPE html>
<html lang="en">
<head>
<meta charset="utf-8">
<title>Meridale Capital Partners Ltd</title>
<link href="https://fonts.googleapis.com/css2?family=Arimo:wght@400;700&family=Open+Sans:wght@400;600&display=swap" rel="stylesheet">
<style>
:root{
  --blue:#1c74c4;
  --topbar:#5b5b5b;
  --text:#333;
  --muted:#9a9a9a;
  --btn:#555;
  --rule:#e6e6e6;
  --footer:#efefef;
  --white:#fff;
}
*{box-sizing:border-box;margin:0;padding:0}
html,body{width:1007px;height:1200px;overflow:hidden;background:var(--white);font-family:Arimo,Arial,sans-serif;color:var(--text)}
.page{position:relative;width:1007px;height:1200px}
.topbar{position:absolute;top:0;left:0;width:100%;height:32px;background:var(--topbar)}
.topbar__links{position:absolute;left:681px;top:11px;font-size:11px;color:var(--white)}
.topbar__login{position:absolute;left:747px;top:7px;width:59px;height:21px;background:var(--blue);color:var(--white);font-size:11px;font-weight:700;text-align:center;line-height:21px}
.header{position:absolute;top:32px;left:0;width:100%;height:64px;background:linear-gradient(#fff,#f1f1f1)}
.brand{position:absolute;left:158px;top:23px;display:flex;align-items:center;gap:8px;color:var(--blue);font-size:17px}
.brand__mark{width:14px;height:14px;background:var(--blue)}
.nav{position:absolute;right:158px;top:27px;display:flex;gap:26px;font-size:14px;color:#444}
.nav a.is-active{color:var(--blue)}
.hero{position:absolute;top:96px;left:0;width:100%;height:358px;background:var(--blue)}
.hero__slide{position:absolute;left:157px;top:30px;width:693px;height:294px;background:var(--white)}
.hero__photo{position:absolute;left:0;top:0;width:430px;height:294px;background:linear-gradient(90deg,#c9c6c2 0%,#b7aea5 55%,#fff 100%)}
.hero__text{position:absolute;left:434px;top:48px;width:255px;font-family:"Open Sans",sans-serif;font-size:10px;line-height:19.2px;color:#444;white-space:nowrap}
.hero__text p+p{margin-top:19px}
.hero__dots{position:absolute;left:488px;top:338px;display:flex;gap:3px}
.hero__dots span{width:11px;height:11px;border-radius:50%;background:#333}
.hero__dots span:first-child{background:var(--white)}
.section-title{position:absolute;top:466px;width:100%;text-align:center;font-size:18px;font-weight:700;color:var(--blue)}
.solution{position:absolute;top:500px;width:222px}
.solution__img{height:125px}
.solution h3{margin-top:19px;font-size:11px;color:var(--blue)}
.solution p{margin-top:5px;font-size:10.5px;line-height:17.6px;color:var(--muted);white-space:nowrap}
.btn{display:inline-block;margin-top:0;margin-left:-2px;width:82px;height:24px;background:var(--btn);color:var(--white);font-size:10px;font-weight:700;text-align:center;line-height:24px}
.rule{position:absolute;left:157px;width:692px;height:1px;background:var(--rule)}
.stat{position:absolute;top:818px;display:flex;gap:20px}
.stat__mark{font-size:26px;color:var(--blue);line-height:48px;width:68px}
.stat__num{font-size:27px;color:#666;text-align:right}
.stat__cap{font-size:11px;color:#666;text-align:right}
.signin{position:absolute;left:742px;top:823px;width:95px;height:41px;background:var(--blue);color:var(--white);font-size:14px;text-align:center;line-height:41px}
.press{position:absolute;top:908px;left:165px;width:680px;display:flex;justify-content:space-between;align-items:center;font-size:12px;color:#555}
.footer{position:absolute;top:961px;left:0;width:100%;height:239px;background:var(--footer)}
.fcol{position:absolute;top:22px}
.fcol h4{font-size:13px;color:#444;margin-bottom:34px}
.fcol li{list-style:none;font-size:11px;color:#333;margin-bottom:11px}
.newsletter input{display:block;width:222px;height:31px;border:0;background:var(--white);padding-left:10px;font-size:10px;color:#bbb;font-family:inherit}
.newsletter .sub{display:inline-block;margin-top:9px;width:62px;height:22px;background:var(--blue);color:var(--white);font-size:11px;font-weight:700;text-align:center;line-height:22px}
.contact-mail{display:flex;align-items:center;gap:7px;font-size:12px;color:#333}
.copyright{position:absolute;top:1143px;width:100%;text-align:center;font-size:11px;color:#333}
</style>
</head>
<body>
<div class="page">
  <div class="topbar">
    <span class="topbar__links">Join &nbsp;| &nbsp;Help</span>
    <span class="topbar__login">Login</span>
  </div>
  <header class="header">
    <div class="brand"><span class="brand__mark"></span>Meridale Capital Partners Ltd</div>
    <nav class="nav"><a class="is-active">Why Alternative ?</a><a>Solutions</a><a>Contact Us</a></nav>
  </header>
  <section class="hero">
    <div class="hero__slide">
      <div class="hero__photo" role="img" aria-label="Photo of business colleagues working together at laptops in an office"></div>
      <div class="hero__text">
        <p>We provide "Sales Aid Finance" through<br>MERIDALE financial and contract solutions.<br>Specialising in the Print and Technology markets,<br>we offer Value Added Resellers (VARs)<br>a range of innovative, cost effective, value added<br>contract and finance options to<br>enhance their sales.</p>
        <p>Our solutions are fully financed and we are totally<br>independent from any AR,technology provider or<br>traditional finance house.</p>
      </div>
    </div>
    <div class="hero__dots"><span></span><span></span><span></span><span></span></div>
  </section>
  <h2 class="section-title">Our Solutions</h2>
  <article class="solution" style="left:157px">
    <div class="solution__img" role="img" aria-label="Photo of hands using a tablet showing charts on a desk" style="background:linear-gradient(135deg,#d8b98f,#e9dcc9)"></div>
    <h3>Managed Services Solutions</h3>
    <p>Lorem Ipsum is simply dummy text of the<br>printing and typesetting industry. Lorem Ipsum<br>has been the industry's standard dummy text<br>ever since the 1500s, when an unknown printer</p>
    <span class="btn">Learn More</span>
  </article>
  <article class="solution" style="left:393px">
    <div class="solution__img" role="img" aria-label="Photo of a smiling professional with colleagues in a meeting behind" style="background:linear-gradient(90deg,#b9cde0,#e8e4df)"></div>
    <h3>Public Sector Solutions</h3>
    <p>Lorem Ipsum is simply dummy text of the<br>printing and typesetting industry. Lorem Ipsum<br>has been the industry's standard dummy text<br>ever since the 1500s, when an unknown printer</p>
    <span class="btn">Learn More</span>
  </article>
  <article class="solution" style="left:629px">
    <div class="solution__img" role="img" aria-label="Photo of a teacher presenting at a whiteboard to students" style="background:linear-gradient(135deg,#8c7463,#c9c8c6 60%,#4aa8d8)"></div>
    <h3>Education Solutions</h3>
    <p>Lorem Ipsum is simply dummy text of the<br>printing and typesetting industry. Lorem Ipsum<br>has been the industry's standard dummy text<br>ever since the 1500s, when an unknown printer</p>
    <span class="btn">Learn More</span>
  </article>
  <div class="rule" style="top:790px"></div>
  <div class="stat" style="left:158px">
    <div class="stat__mark">MCP</div>
    <div><div class="stat__num">29,412 investors</div><div class="stat__cap">in the UK have lent to businesses</div></div>
  </div>
  <div class="stat" style="left:463px">
    <div class="stat__mark">MCP</div>
    <div><div class="stat__num">£286,006,160</div><div class="stat__cap">lent to British businesses</div></div>
  </div>
  <span class="signin">Sign In</span>
  <div class="rule" style="top:883px"></div>
  <div class="press">
    <span>Harbor Business Review</span><span>Ledgerline</span><span>Westbay Broadcast</span><span>Market Insider Daily</span><span>CircuitWire</span><span>Coastal Times</span>
  </div>
  <footer class="footer">
    <div class="fcol" style="left:156px"><h4>Home</h4><ul><li>Why Alternative ?</li><li>Solutions</li><li>Contact Us</li></ul></div>
    <div class="fcol" style="left:305px"><h4>Solutions</h4><ul><li>Manages Services Solutions</li><li>Public Sector Solutions</li><li>Educarion Solutions</li></ul></div>
    <div class="fcol newsletter" style="left:451px;top:24px"><h4 style="margin-bottom:30px">Sign Up Newsletter</h4><input value="Enter The E-Mail Address" aria-label="Email address"><span class="sub">Subscribe</span></div>
    <div class="fcol" style="left:693px;top:24px"><h4 style="margin-bottom:32px">Contact Us</h4>
      <div class="contact-mail"><svg width="21" height="15" viewBox="0 0 21 15"><rect x="0.5" y="0.5" width="20" height="14" fill="#555" stroke="#555"/><path d="M1 1l9.5 8L20 1M1 14l7-6M20 14l-7-6" stroke="#efefef" fill="none"/></svg>info@meridalecp.co.uk</div>
      <h4 style="margin-top:10px">Connect With Us</h4>
    </div>
  </footer>
  <p class="copyright">© 2014 Compnay Name,All Rights Reserved</p>
</div>
</body>
</html>
```